New letter head for Air Conditioning business

We need a new professional letter head design to suit our new re-branded air conditioning business. Our new logo is attached

```html
<!DOCTYPE html>
<html lang="en">
<head>
<meta charset="utf-8">
<title>Norvane Letterhead</title>
<link href="https://fonts.googleapis.com/css2?family=Exo+2:wght@500;600&display=swap" rel="stylesheet">
<style>
  :root {
    --paper: #fefefe;
    --green: #68c48a;
    --charcoal: #404042;
    --coral: #f17163;
    --white: #ffffff;
  }
  * { margin: 0; padding: 0; box-sizing: border-box; }
  html, body { width: 848px; height: 1200px; overflow: hidden; background: var(--paper); }
  .letterhead {
    position: relative;
    width: 848px;
    height: 1200px;
    background: var(--paper);
    font-family: "Exo 2", sans-serif;
  }
  .brand {
    position: absolute;
    top: 62px;
    left: 0;
    width: 848px;
    display: flex;
    justify-content: center;
    align-items: center;
    gap: 16px;
  }
  .brand-mark {
    width: 34px;
    height: 34px;
    background: var(--green);
  }
  .brand-name {
    font-family: "Exo 2", sans-serif;
    font-weight: 600;
    font-size: 48px;
    letter-spacing: 8px;
    color: var(--charcoal);
    line-height: 1;
  }
  .accent-band {
    position: absolute;
    top: 1101px;
    left: 0;
    width: 848px;
    height: 15px;
    background: var(--green);
  }
  .contact-bar {
    position: absolute;
    top: 1116px;
    left: 0;
    width: 848px;
    height: 84px;
    background: var(--charcoal);
  }
  .contact-item {
    position: absolute;
    top: 32px;
    display: flex;
    align-items: center;
    gap: 15px;
    color: var(--white);
    font-weight: 500;
    font-size: 11.5px;
    letter-spacing: 0.3px;
    line-height: 14px;
  }
  .contact-item.phone { left: 70px; }
  .contact-item.email { left: 317px; }
  .contact-item.address { left: 569px; }
  .contact-icon {
    width: 20px;
    height: 20px;
    border-radius: 5px;
    background: var(--coral);
    display: flex;
    align-items: center;
    justify-content: center;
    flex-shrink: 0;
  }
  .contact-icon svg { width: 12px; height: 12px; }
</style>
</head>
<body>
<main class="letterhead">
  <header class="brand">
    <span class="brand-mark"></span>
    <span class="brand-name">NORVANE</span>
  </header>

  <div class="accent-band"></div>

  <footer class="contact-bar">
    <div class="contact-item phone">
      <span class="contact-icon">
        <svg viewBox="0 0 24 24"><path fill="#fff" d="M3 9c0-3 4-5 9-5s9 2 9 5v1.5h-4.5V8.5c-1.5-.6-3-.8-4.5-.8s-3 .2-4.5.8v2H3zM7 12h10l3 6.5c0 .8-.6 1.5-1.5 1.5h-13c-.9 0-1.5-.7-1.5-1.5zm5 1.8a2.4 2.4 0 1 0 0 4.8 2.4 2.4 0 0 0 0-4.8z"/></svg>
      </span>
      <span>+0000 0000000<br>+0000 0000000</span>
    </div>
    <div class="contact-item email">
      <span class="contact-icon">
        <svg viewBox="0 0 24 24"><path fill="#fff" d="M2 5h20v14H2zm2 2v.5l8 5.5 8-5.5V7z"/></svg>
      </span>
      <span>info@norvane air condition</span>
    </div>
    <div class="contact-item address">
      <span class="contact-icon">
        <svg viewBox="0 0 24 24"><path fill="#fff" d="M12 1.5a7.5 7.5 0 0 0-7.5 7.5c0 5.5 7.5 13.5 7.5 13.5s7.5-8 7.5-13.5A7.5 7.5 0 0 0 12 1.5zm0 4.5a3 3 0 1 1 0 6 3 3 0 0 1 0-6z"/></svg>
      </span>
      <span>Post Box: 418205, Dubai, UAE</span>
    </div>
  </footer>
</main>
</body>
</html>
```